Brochure Design Project

A4 Portrait
8 Page Sales brochure for Automatic Coffee Machines for Offices.
We have 4 products in 4 cateries.
Small Office
Medium Office
Large Office
Whole Company / Food Service.

There will be a product image plus 3-4 accessories for each product

Then a brief sales pitch text for each product.

We supply to public listed companies therefore it has to be professional, well presented and eye catching.

Thank you
Updates

I will make the budget $200

Project Deadline Extended

Hello,

Please note that I've made changes to the job brief. 

Thanks

Walter 

Hi 

Please find attached contents in pdf for your implementation.

1. Small Office Solution
2. Medium Office Solution 
3. Large Office Solution
4. Whole Company Solution
5. Food Service

Thanks 

Walter

Project Deadline Extended

Hi All

Budget increased to $200, extended project by 7 more days.

Thank you

Howard Benlo

Target Market(s)

Big Corporate Companies in major Australian cities

Industry/Entity Type

It Company

Requirements
Must have
• A4 Portrait
8 Page photo and sales pitch text. One product per page starting from 3nd page
5 products into 5 categories of

Page 2 will tell about our company and services

Small Office Solution (page 3)
$16 per day)

Medium Office Solution (page 4)
$18 per day)

Large Office Solution (page 5)
$19 per day)

Whole Company (page 6)
$24 per day)

Food Service Solution (page 7
$28 per day

Each product page will highlight
eg
Small Office Solution
$16 per day)

Each page will have 3-4 accessories (photos)

Page 8 Our logo, address & Conatct details - Please see for contact details http://www.brewvanta.com.au/brew_va
Nice to have
• Logo, photo of coffee machine, an office environment where people are kind of enjoying coffee in a lounge.

Should not have
• Not messy, no old style,

```html
<!DOCTYPE html>
<html lang="en">
<head>
<meta charset="utf-8">
<title>Brewvanta – Medium Office Solution</title>
<link rel="stylesheet" href="https://fonts.googleapis.com/css2?family=Arimo:wght@400;700&family=Pinyon+Script&display=swap">
<style>
  :root {
    --maroon: #4a1414;
    --amber: #f6a71f;
    --cream: #fcf4c5;
    --brand-red: #e0222a;
    --ink: #2a2a2a;
    --heading: #3a1f14;
    --white: #ffffff;
  }
  * { margin: 0; padding: 0; box-sizing: border-box; }
  html, body { width: 848px; height: 1200px; overflow: hidden; }
  body {
    position: relative;
    background: var(--cream);
    font-family: "Arimo", Arial, sans-serif;
    color: var(--ink);
    font-size: 10.5px;
    line-height: 13.6px;
  }
  .header-band { position: absolute; left: 0; top: 0; width: 848px; height: 178px; background: var(--maroon); }
  .accent-stripe { position: absolute; left: 0; top: 178px; width: 848px; height: 14px; background: var(--amber); }

  .brand-box {
    position: absolute; left: 664px; top: 47px; width: 134px; height: 81px;
    background: var(--brand-red); border-radius: 4px;
    display: flex; flex-direction: column; align-items: center; justify-content: center; gap: 4px;
    color: var(--white);
  }
  .brand-name { font-size: 19px; line-height: 20px; font-weight: 400; }
  .brand-tagline { font-size: 6.5px; line-height: 8px; letter-spacing: .3px; text-transform: uppercase; }

  .intro-column { position: absolute; left: 93px; top: 247px; width: 296px; }
  .intro-column p { margin-bottom: 13.6px; }
  .spec-list, .drink-list { list-style: none; }
  .spec-list li, .drink-list li { position: relative; padding-left: 20px; }
  .spec-list li::before, .drink-list li::before {
    content: "•"; position: absolute; left: 0; top: 0;
  }
  .spec-list .sub { display: block; }
  .drinks-heading { list-style: none; margin: 13px 0 14px; }
  .drinks-heading li { position: relative; padding-left: 20px; font-size: 11.5px; }
  .drinks-heading li::before { content: "•"; position: absolute; left: 0; }

  .script { font-family: "Pinyon Script", cursive; font-weight: 400; color: var(--heading); }
  .features-title { position: absolute; left: 91px; top: 630px; font-size: 36px; line-height: 40px; }
  .solution-title { position: absolute; left: 493px; top: 256px; font-size: 32px; line-height: 36px; }

  .features { position: absolute; left: 93px; top: 668px; width: 296px; }
  .feature { text-align: justify; margin-bottom: 13px; }
  .feature h3 { font-weight: 400; font-size: 12.3px; line-height: 14px; text-transform: uppercase; color: var(--ink); text-align: left; }

  .price-badge {
    position: absolute; left: 562px; top: 299px; width: 108px; height: 108px;
    border-radius: 50%; background: var(--brand-red);
    color: var(--white); text-align: center;
    font-family: "Pinyon Script", cursive;
    display: flex; flex-direction: column; align-items: center; justify-content: center;
  }
  .price-amount { font-size: 44px; line-height: 40px; font-weight: 400; }
  .price-period { font-size: 22px; line-height: 22px; }

  .photo { position: absolute; }
  .photo-machine {
    left: 541px; top: 395px; width: 163px; height: 355px;
    background: linear-gradient(180deg, #6d6d6d 0%, #1e1e1e 40%, #3b3b3b 70%, #151515 100%);
    border-radius: 3px;
  }
  .photo-cup-rack {
    left: 553px; top: 848px; width: 124px; height: 231px;
    background: linear-gradient(180deg, #d8d8d8 0%, #9a9a9a 50%, #5a5a5a 100%);
  }
  .accent-square { position: absolute; left: 677px; top: 848px; width: 171px; height: 181px; background: var(--amber); }
  .photo-lounge {
    left: 507px; top: 1029px; width: 171px; height: 171px;
    background: linear-gradient(135deg, #d7a46a 0%, #9b6132 50%, #5c3517 100%);
  }
</style>
</head>
<body>
  <div class="header-band"></div>
  <div class="accent-stripe"></div>

  <div class="brand-box">
    <span class="brand-name">Brewvanta</span>
    <span class="brand-tagline">Automatic Coffee Machines</span>
  </div>

  <section class="intro-column">
    <p>Coffee and Hot Chocolate in Perfect Sync<br>where quality and reliability are key.</p>
    <p>Dimension: (coffee machine)<br>W: 430 D: 500 H: 695</p>
    <ul class="spec-list">
      <li>Fresh Coffee</li>
      <li>Fresh Milk</li>
      <li>Automatic Cleaning Program<span class="sub">no parts removed,</span><span class="sub">no manuals required</span></li>
      <li>30 Drinks of your choice</li>
      <li>Easy Operation</li>
      <li>Fast and Quiet</li>
      <li>Robust Body &amp; Metal Brewer</li>
      <li>HACCP Certified</li>
    </ul>
    <ul class="drinks-heading"><li>CAFE QUALITY DRINKS</li></ul>
    <ul class="drink-list">
      <li>Up to 30 selections including:</li>
      <li>Cappuccino</li>
      <li>Hot Chocolate</li>
      <li>Espresso</li>
      <li>Latte</li>
      <li>Mocha</li>
      <li>Chai Latte</li>
      <li>Strength and cup size options</li>
    </ul>
  </section>

  <h2 class="script features-title">Features</h2>
  <section class="features">
    <div class="feature">
      <h3>Fresh Coffee - Micro Fine Sieve</h3>
      <p>The Micro-Fine Sieve is a key guarantee for optimal coffee. Over 45,150 conical holes across an area of 1075 mm2. This ensures dreg-free and high quality coffee with optimum extraction.</p>
    </div>
    <div class="feature">
      <h3>Fully Automatic Milk Cleaning Program-</h3>
      <p>HACCP Certified Milk &amp; Coffee systems are cleaned Automatically. There's no removal of parts and components. The only company that is HACCP tested and certified.</p>
    </div>
    <div class="feature">
      <h3>Easy Operation - Graphic Display:</h3>
      <p>30 Drink selections of your choice, never before has real coffee preparation been so simple and fast to prepare with the flair of a trained Barista.</p>
    </div>
    <div class="feature">
      <h3>Hot Chocolate and Chai Latte Maker</h3>
      <p>Integrated Chocolate and Chai Latte module provides you with the option to dispense different Coffee, Chocolate and Chai specialities with milk. There's something for everyone.</p>
    </div>
    <div class="feature">
      <h3>Choices</h3>
      <p>Strength of drinks can be programed in 3 levels of Mild, Medium and Strong. Easy access to Small, Medium and Large cups are also available on the one screen</p>
    </div>
  </section>

  <h1 class="script solution-title">Medium Office Solution</h1>

  <div class="photo photo-machine" role="img" aria-label="Photo of the automatic coffee machine with bean hoppers and touch display"></div>

  <div class="price-badge">
    <span class="price-amount">$18</span>
    <span class="price-period">per day</span>
  </div>

  <div class="photo photo-cup-rack" role="img" aria-label="Photo of the cup warmer accessory stacked with white cups"></div>
  <div class="accent-square"></div>
  <div class="photo photo-lounge" role="img" aria-label="Photo of office staff enjoying coffee together"></div>
</body>
</html>
```